Exclusive Pet groomer Post Card

We need a design for a direct mailing postcard. We want to include images of some of dogs and cats done the list of our services and the benefits of our company.

I like something like: Does your pet look like any of these or is a similar breed?

If your answer is yes, then it deserves the best groomer in town

any ideas are welcome!

URGENT Mailing Postcard needed!

Elegant, modern and clean sophisticated card that has images of the dogs and cats provided. I will use the original images from the image bank once the project is approved. As a designer you just need to create the layout for this and the organization!

Thanks

Target Market(s)

High Income professionals that will pay for premium services for their pets.

Industry/Entity Type

Pet

Requirements
Must have
• A full color double sided postcard. 5.5 x 8.5 in postcard. (I want to have all pics uploaded. I used some sample images from stock photo but once approved I will purchase the images at the respective site). Must have space to place recipient address and space for NPDS stamp. ( is a postcard to be mailed!)

I would like to have the following text in the post card:

Enhance the beauty of your pets
Pamper your best friend
Give to your dog or cat the stylish treatment it deserves

One of the top groomers in town
Experienced in dogs and cats
Clean individual pet grooming stations (Sanitation and Sterilization)
Services:
Full service grooming* services for dogs and cats include:
Day Spa, High Fashion Haircuts, hair trimming, nail clipping and “Petticures”
Bathing, gentle ear Cleaning, sanitary trim, Brushing, Fluff Drying and Dematting
* Regular grooming ensures happier and healthier pets

Fur Harbor Trim
2716 NE 147th Street, North Miami, Florida 33181
T. 305-647-3918
www.furharbortrim.example
Nice to have
• Logo as in the website

```html
<!DOCTYPE html>
<html lang="en">
<head>
<meta charset="utf-8">
<title>Fur Harbor Trim – Mailing Postcard</title>
<link rel="stylesheet" href="https://fonts.googleapis.com/css2?family=Handlee&display=swap">
<style>
  :root {
    --page: #ffffff;
    --card: #a898b5;
    --ink: #ffffff;
    --accent: #b04fa6;
  }
  html, body {
    margin: 0;
    padding: 0;
    width: 1200px;
    height: 851px;
    overflow: hidden;
    background: var(--page);
  }
  .postcard {
    position: absolute;
    left: 21px;
    top: 19px;
    width: 1150px;
    height: 806px;
    background: var(--card);
    font-family: "Handlee", cursive;
    color: var(--ink);
  }
  .message {
    position: absolute;
    left: 12px;
    top: 14px;
    width: 560px;
    text-align: center;
    font-size: 23px;
    line-height: 32px;
  }
  .message p { margin: 0 0 14px; }
  .message .greeting { margin-bottom: 10px; }
  .message .intro-label { margin: 26px 0 22px; }
  .address {
    font-size: 27px;
    line-height: 40px;
    margin-top: 0;
  }
  .address .web { font-size: 24px; }
  .sign-off {
    position: absolute;
    left: 195px;
    top: 752px;
    font-size: 23px;
  }
  .paw-mark {
    position: absolute;
    left: 355px;
    top: 726px;
  }
  .divider {
    position: absolute;
    left: 594px;
    top: 16px;
    width: 3px;
    height: 778px;
    background: repeating-linear-gradient(to bottom, var(--ink) 0 18px, transparent 18px 34px);
  }
  .stamp-box {
    position: absolute;
    left: 777px;
    top: 35px;
    width: 331px;
    height: 210px;
    background: var(--ink);
  }
  .address-lines {
    position: absolute;
    left: 615px;
    top: 356px;
    width: 491px;
  }
  .address-lines span {
    display: block;
    height: 4px;
    background: var(--ink);
    margin-bottom: 64px;
  }
  .brand {
    position: absolute;
    left: 740px;
    top: 708px;
    display: flex;
    align-items: center;
    gap: 16px;
  }
  .brand-dot {
    width: 46px;
    height: 46px;
    border-radius: 50%;
    background: var(--ink);
  }
  .brand-name {
    font-size: 34px;
    color: var(--ink);
  }
</style>
</head>
<body>
  <main class="postcard">
    <section class="message">
      <p class="greeting">Dear human mom and dad,</p>
      <p>I just smelled some exciting news: there is a place in our town where I could experience stylish treatments:</p>
      <p>Full service grooming, day spa, high fashion haircuts, nail clipping and "petticures", bathing, gentle ear cleaning, sanitary trim, brushing, fluff drying and dematting.</p>
      <p>I think I deserve to be pampered, so please take me there as soon as possible.</p>
      <p class="intro-label">Here is the address:</p>
      <p class="address">Fur Harbor Trim<br>
        2716 NE 147th Street, North Miami,<br>
        Florida 33181<br>
        Phone: 305-647-3918<br>
        <span class="web">www.furharbortrim.example</span></p>
    </section>
    <p class="sign-off" style="margin:0">Yours beloved,</p>
    <svg class="paw-mark" width="66" height="66" viewBox="0 0 66 66" role="img" aria-label="Paw print signature">
      <ellipse cx="33" cy="40" rx="30" ry="24" fill="#ffffff"/>
    </svg>

    <div class="divider" aria-hidden="true"></div>

    <div class="stamp-box" aria-label="Stamp area"></div>
    <div class="address-lines" aria-label="Recipient address lines">
      <span></span><span></span><span></span><span></span><span></span>
    </div>

    <div class="brand">
      <span class="brand-dot" aria-hidden="true"></span>
      <span class="brand-name">Fur Harbor Trim</span>
    </div>
  </main>
</body>
</html>
```